Talbek vodka

With the logo attached in the subsequent file, a business card that reflects a premium and organic vodka. On the first side, the company logo in large. The names must be included on the back of the card (Mateo Ignacio Dalmau Ferrerons with the number +34 655 219 870 and Oriol Batlle Quintana and +34 677 341 592). The slogan "What binds us" and "Organic and permium vodka" in bold E-mail (talbekvodka@mailora.net); Website www.talbekvodkaorg.net

```html
<!DOCTYPE html>
<html lang="en">
<head>
<meta charset="utf-8">
<title>Talbek vodka – business card</title>
<link href="https://fonts.googleapis.com/css2?family=Cinzel:wght@400;600;700&family=Cormorant+Garamond:wght@500;600&display=swap" rel="stylesheet">
<style>
  :root {
    --backdrop: #3a3a3a;
    --card: #fbfbfb;
    --ink: #6e6e72;
    --ink-dark: #3c3c40;
    --panel: #2d2d2f;
    --panel-faint: #3a3a3d;
    --stripe: #8c8c92;
    --slogan: #f2f2f2;
    --tagline: #8f8f93;
  }
  * { box-sizing: border-box; margin: 0; padding: 0; }
  html, body { width: 1163px; height: 1200px; overflow: hidden; }
  body {
    background: var(--backdrop);
    display: flex;
    flex-direction: column;
    align-items: center;
    justify-content: center;
    gap: 40px;
    font-family: "Cormorant Garamond", Georgia, serif;
  }
  .card {
    width: 940px;
    height: 534px;
    background: var(--card);
    position: relative;
    overflow: hidden;
    box-shadow: 0 6px 18px rgba(0,0,0,.35);
  }

  /* Front */
  .card--front {
    display: flex;
    flex-direction: column;
    align-items: center;
    justify-content: center;
  }
  .brand-name {
    font-family: "Cinzel", Georgia, serif;
    font-weight: 400;
    font-size: 112px;
    line-height: 1;
    color: var(--ink);
    letter-spacing: 2px;
    margin-top: 10px;
  }
  .front-web {
    margin-top: 70px;
    font-family: "Cinzel", Georgia, serif;
    font-size: 21px;
    letter-spacing: 7px;
    color: var(--ink-dark);
  }

  /* Back */
  .card--back { display: flex; }
  .slogan-panel {
    width: 452px;
    height: 100%;
    background: var(--panel);
    display: flex;
    flex-direction: column;
    align-items: center;
    padding-top: 140px;
  }
  .brand-name--faint {
    font-size: 72px;
    color: var(--panel-faint);
  }
  .slogan {
    margin-top: 46px;
    font-family: "Cinzel", Georgia, serif;
    font-weight: 400;
    font-size: 42px;
    color: var(--slogan);
  }
  .tagline {
    margin-top: 10px;
    font-family: "Cinzel", Georgia, serif;
    font-size: 19px;
    color: var(--tagline);
  }
  .stripe { width: 14px; height: 100%; background: var(--stripe); }
  .contacts {
    flex: 1;
    padding: 66px 0 0 40px;
    color: var(--ink-dark);
  }
  .person-name {
    font-family: "Cinzel", Georgia, serif;
    font-weight: 700;
    font-size: 26px;
    line-height: 1.2;
    color: var(--ink);
  }
  .contact-line {
    display: flex;
    align-items: center;
    gap: 14px;
    font-size: 22px;
    margin-top: 16px;
  }
  .contact-line svg { width: 22px; height: 22px; flex: none; }
  .contact-line--caps {
    font-family: "Cinzel", Georgia, serif;
    font-size: 20px;
    margin-top: 10px;
  }
  .person + .person { margin-top: 34px; }
  .web-block { margin-top: 42px; }
</style>
</head>
<body>
  <section class="card card--front">
    <h1 class="brand-name">Talbek</h1>
    <p class="front-web">WWW.TALBEKVODKAORG.NET</p>
  </section>

  <section class="card card--back">
    <div class="slogan-panel">
      <p class="brand-name brand-name--faint">Talbek</p>
      <p class="slogan">What binds us</p>
      <p class="tagline">Organic and permium vodka</p>
    </div>
    <div class="stripe"></div>
    <div class="contacts">
      <div class="person">
        <p class="person-name">Mateo Ignacio<br>Dalmau Ferrerons</p>
        <p class="contact-line">
          <svg viewBox="0 0 24 24"><circle cx="12" cy="12" r="12" fill="#6e6e72"/><path d="M8.2 6.5l2 2.4-1.2 1.5c.8 1.7 2 2.9 3.7 3.7l1.5-1.2 2.4 2-1.3 1.8c-4.1-.6-8-4.5-8.6-8.6z" fill="#fff"/></svg>
          +34 655 219 870
        </p>
      </div>
      <div class="person">
        <p class="person-name">Oriol Batlle Quintana</p>
        <p class="contact-line">
          <svg viewBox="0 0 24 24"><circle cx="12" cy="12" r="12" fill="#6e6e72"/><path d="M8.2 6.5l2 2.4-1.2 1.5c.8 1.7 2 2.9 3.7 3.7l1.5-1.2 2.4 2-1.3 1.8c-4.1-.6-8-4.5-8.6-8.6z" fill="#fff"/></svg>
          +34 677 341 592
        </p>
      </div>
      <div class="web-block">
        <p class="contact-line contact-line--caps">
          <svg viewBox="0 0 24 24"><circle cx="12" cy="12" r="12" fill="#6e6e72"/><rect x="6.5" y="8" width="11" height="8" rx="1" fill="#fff"/><path d="M6.8 8.4l5.2 4 5.2-4" fill="none" stroke="#6e6e72" stroke-width="1.2"/></svg>
          TALBEKVODKA@MAILORA.NET
        </p>
        <p class="contact-line contact-line--caps">
          <svg viewBox="0 0 24 24"><circle cx="12" cy="12" r="12" fill="#6e6e72"/><g fill="none" stroke="#fff" stroke-width="1.2"><circle cx="12" cy="12" r="6"/><ellipse cx="12" cy="12" rx="2.6" ry="6"/><path d="M6 12h12"/></g></svg>
          WWW.TALBEKVODKAORG.NET
        </p>
      </div>
    </div>
  </section>
</body>
</html>
```